A4 advert for Market Quill editorial offer

I am the publisher of online site www.tradeledger.co.uk, as part of the commercial parts of the website I sell commercial licenses to PR people and marketeers who want to publish editorials onto my site.
I want an A4 visual flyer to help me send to people that have enquired about this offering. At the moment I send a simple emial with screen shots. I do however have a media pack for other advertising parts of the digital newspaper. I will upload this as part of the project to help give you an idea of how the online paper works.
Okay here is the content for the flyer..
Publish content directly onto the Market Quill server
The price is £250 per year paid by electronic direct debit.
As part of your membership you get the following:
Create and publish articles on Market Quill
Include hyperlinks back to your own website
A free company report page (similar to knowpedia)
Social logins - Allows you to sync your social media to your published articles, we also add you to our social media feeds which means as your articles are published we post them and send them to workmesh
Create and publish blogs
Upload resources or guides to our resource library

```html
<!DOCTYPE html>
<html lang="en">
<head>
<meta charset="utf-8">
<title>Market Quill – Editorial Membership Flyer</title>
<link rel="stylesheet" href="https://fonts.googleapis.com/css2?family=Cinzel:wght@400;600&family=Arimo:ital,wght@0,400;0,700;1,700&family=Archivo+Black&display=swap">
<style>
  :root {
    --page-bg: #e4e4e6;
    --paper: #f3f3f4;
    --paper-shade: #e6e6e8;
    --maroon: #7d1538;
    --maroon-light: #9a2349;
    --maroon-soft: #8c2f4b;
    --navy: #1f2f5e;
    --ink: #111111;
    --white: #ffffff;
  }
  * { margin: 0; padding: 0; box-sizing: border-box; }
  html, body {
    width: 1200px; height: 1000px; overflow: hidden;
    background: var(--page-bg);
  }
  .flyer {
    position: absolute; left: 322px; top: 104px;
    width: 557px; height: 744px; overflow: hidden;
    background: radial-gradient(ellipse at 40% 45%, var(--paper) 0%, var(--paper-shade) 100%);
    font-family: "Arimo", Arial, sans-serif;
    color: var(--ink);
  }
  .flyer__shapes { position: absolute; inset: 0; }
  .header-band {
    position: absolute; left: 0; top: 70px; width: 557px; height: 110px;
    background: radial-gradient(ellipse at 50% 60%, var(--maroon-light) 0%, var(--maroon) 70%);
    color: var(--white);
    font-family: "Cinzel", "Times New Roman", serif;
    text-align: center;
    box-shadow: 0 4px 8px rgba(0,0,0,.18);
  }
  .header-band__lead {
    position: absolute; top: 22px; width: 100%;
    font-size: 21px; letter-spacing: 1.5px; font-weight: 400;
  }
  .header-band__main {
    position: absolute; top: 52px; width: 100%;
    font-size: 29px; letter-spacing: 1px; font-weight: 600;
  }
  .price {
    position: absolute; left: 0; width: 557px; top: 206px; text-align: center;
  }
  .price__intro { font-size: 21px; line-height: 26px; margin-left: -6px; }
  .price__amount {
    font-family: "Archivo Black", "Arial Black", sans-serif;
    font-size: 60px; line-height: 68px; color: var(--navy);
    letter-spacing: -2px; margin-left: -6px;
  }
  .price__terms { font-size: 16px; line-height: 20px; margin-left: 12px; }
  .benefits {
    position: absolute; left: 43px; top: 342px; width: 340px;
    font-size: 12.4px; line-height: 17px;
  }
  .benefits__title { font-weight: 700; font-style: italic; font-size: 13px; margin-bottom: 4px; }
  .benefits__list { list-style: none; }
  .benefits__gap { margin-top: 11px; }
  .brand {
    position: absolute; left: 234px; top: 654px;
    font-family: "Arimo", Arial, sans-serif; font-weight: 700;
    font-size: 38px; color: var(--white); letter-spacing: -0.5px;
  }
</style>
</head>
<body>
  <main class="flyer">
    <svg class="flyer__shapes" width="557" height="744" viewBox="0 0 557 744">
      <defs>
        <linearGradient id="cornerFill" x1="1" y1="0" x2="0.3" y2="1">
          <stop offset="0" stop-color="#7a1a3a"/>
          <stop offset="0.5" stop-color="#9a2d4c"/>
          <stop offset="1" stop-color="#7a2138"/>
        </linearGradient>
      </defs>
      <polygon class="ribbon" points="115,0 220,0 0,308 0,196" fill="var(--maroon-soft)"/>
      <polygon class="ribbon-top" points="115,0 220,0 170,70 65,70" fill="var(--maroon)"/>
      <polygon class="corner-panel" points="557,200 557,744 149,744" fill="url(#cornerFill)"
               role="img" aria-label="Faint archery target with a dart in the bullseye"/>
    </svg>

    <header class="header-band">
      <p class="header-band__lead">Publish content directly onto</p>
      <h1 class="header-band__main">the Market Quill server</h1>
    </header>

    <section class="price">
      <p class="price__intro">The price is</p>
      <p class="price__amount">£250</p>
      <p class="price__terms">paid by electronic direct debit</p>
    </section>

    <section class="benefits">
      <h2 class="benefits__title">As part of your membership you get the following:</h2>
      <ul class="benefits__list">
        <li>Create and publish articles on Market Quill</li>
        <li>Include hyperlinks back to your own website</li>
        <li>A free company report page (similar to knowpedia)</li>
        <li class="benefits__gap">Social logins - Allows you to sync your social media to your<br>published articles, we also add you to our social media<br>feeds which means as your articles are published we<br>post them and send them to workmesh Create and<br>publish blogs</li>
        <li>Upload resources or guides to our resource<br>library</li>
      </ul>
    </section>

    <p class="brand">Market Quill</p>
  </main>
</body>
</html>
```